Business Card Design

I need a business card for my company i am starting. I will be providing stump grinding services. I use a motorized machine to grind stumps down under the ground so that they are out of the way and out of sight. I'm looking for my card to have maroon or dark red somewhere in the card to match my truck. I'm going to use this card to advertise and also serve as a design to wrap my truck tailgate as advertisement so i want it to match. the dark maroon color of my truck. I wouldn't mind using bright colors or color for the rest of the card or the lettering or any designs on the card. In the images i have provided i like how there are saw blades integrated into these people advertisements. I also like the illustration of the stump grinder. I also provided a picture of the actual cutting wheel or blade of the grinder.

Industry/Entity Type

Business

Contact Information for Business Card

Company Name - Oakline Stump Grinding
Phone - 407-219-5573
Email - harlow.stumpwork@quillpost.net
Name and title - Thomas Harlow - Owner and operator
Company Slogan - You find them, I'll grind them

```html
<!DOCTYPE html>
<html lang="en">
<head>
<meta charset="utf-8">
<title>Oakline Stump Grinding – Business Card</title>
<link rel="stylesheet" href="https://fonts.googleapis.com/css2?family=Montserrat:wght@800&family=Roboto+Slab:wght@300;400;700&display=swap">
<style>
  :root {
    --maroon: #5a1414;
    --ink: #232323;
    --paper: #ffffff;
    --backdrop: #e9e9e9;
    --on-maroon: #ffffff;
  }
  html, body {
    margin: 0;
    width: 1200px;
    height: 800px;
    overflow: hidden;
    background: var(--backdrop);
  }
  .card {
    position: absolute;
    left: 100px;
    top: 114px;
    width: 1000px;
    height: 572px;
    background: var(--paper);
    overflow: hidden;
    box-shadow: 0 18px 40px rgba(0,0,0,0.18);
  }
  .card-band {
    position: absolute;
    inset: 0;
  }
  .brand {
    position: absolute;
    left: 70px;
    top: 110px;
    display: flex;
    align-items: center;
    gap: 34px;
  }
  .brand-dot {
    width: 150px;
    height: 150px;
    border-radius: 50%;
    background: var(--maroon);
    flex: none;
  }
  .brand-name {
    font-family: "Montserrat", sans-serif;
    font-weight: 800;
    font-size: 58px;
    line-height: 1.02;
    letter-spacing: 1px;
    text-transform: uppercase;
    color: var(--ink);
    margin: 0;
  }
  .brand-rule {
    position: absolute;
    left: 254px;
    top: 250px;
    width: 540px;
    height: 3px;
    background: var(--maroon);
  }
  .slogan {
    position: absolute;
    left: 254px;
    top: 262px;
    margin: 0;
    font-family: "Roboto Slab", serif;
    font-weight: 300;
    font-size: 32px;
    line-height: 1.2;
    color: var(--ink);
  }
  .contact {
    position: absolute;
    left: 340px;
    top: 458px;
    color: var(--on-maroon);
    font-family: "Roboto Slab", serif;
  }
  .contact-name {
    display: flex;
    align-items: baseline;
    gap: 16px;
    margin: 0;
    line-height: 1.1;
  }
  .person {
    font-weight: 700;
    font-size: 40px;
    white-space: nowrap;
  }
  .role {
    font-weight: 400;
    font-size: 17px;
    white-space: nowrap;
  }
  .contact-rule {
    width: 250px;
    height: 2px;
    background: var(--on-maroon);
    margin: 6px 0 10px;
  }
  .email {
    margin: 0;
    font-size: 20px;
    font-weight: 400;
    white-space: nowrap;
  }
  .phone {
    position: absolute;
    left: 730px;
    top: 518px;
    display: flex;
    align-items: center;
    gap: 10px;
    margin: 0;
    font-family: "Roboto Slab", serif;
    font-size: 24px;
    line-height: 1.2;
    color: var(--on-maroon);
    white-space: nowrap;
  }
</style>
</head>
<body>
  <div class="card">
    <svg class="card-band" width="1000" height="572" viewBox="0 0 1000 572" aria-hidden="true">
      <polygon points="0,540 1000,300 1000,572 0,572" fill="var(--maroon)"/>
    </svg>

    <div class="brand">
      <span class="brand-dot"></span>
      <p class="brand-name">Oakline<br>Stump Grinding</p>
    </div>
    <div class="brand-rule"></div>
    <p class="slogan">You find them, I'll grind them</p>

    <div class="contact">
      <p class="contact-name"><span class="person">Thomas Harlow</span><span class="role">Owner and operator</span></p>
      <div class="contact-rule"></div>
      <p class="email">harlow.stumpwork@quillpost.net</p>
    </div>

    <p class="phone">
      <svg width="20" height="20" viewBox="0 0 24 24" aria-hidden="true">
        <path fill="var(--on-maroon)" d="M6.6 10.8a15.1 15.1 0 0 0 6.6 6.6l2.2-2.2a1 1 0 0 1 1-.25 11.4 11.4 0 0 0 3.6.57 1 1 0 0 1 1 1V20a1 1 0 0 1-1 1A17 17 0 0 1 3 4a1 1 0 0 1 1-1h3.5a1 1 0 0 1 1 1c0 1.25.2 2.45.57 3.57a1 1 0 0 1-.25 1z"/>
      </svg>
      407-219-5573
    </p>
  </div>
</body>
</html>
```